kestrova business cards

Hey design gurus!
I'm after a clean, modern, stylish business card for my about to be launched company.
I've uploaded the logos for my company "Kestrova Electrical Solutions"
and also the tarrow alliance logo to whom i am associated.

```html
<!DOCTYPE html>
<html lang="en">
<head>
<meta charset="utf-8">
<title>Kestrova Electrical Solutions – Business Cards</title>
<link href="https://fonts.googleapis.com/css2?family=Michroma&family=Arimo:wght@400&display=swap" rel="stylesheet">
<style>
  :root {
    --stage: #3a3a3c;
    --card-dark: #06141d;
    --card-mid: #15262f;
    --brand-blue: #1a86d0;
    --ring-blue: #0b7cc6;
    --white: #ffffff;
    --emboss: #1c2e38;
    --emboss-light: #2e4653;
    --bronze: #a8564a;
  }
  * { margin: 0; padding: 0; box-sizing: border-box; }
  html, body { width: 1200px; height: 901px; overflow: hidden; }
  body {
    background: radial-gradient(ellipse at 50% 40%, #4a4a4c 0%, var(--stage) 70%);
    font-family: "Arimo", Arial, sans-serif;
    position: relative;
  }
  .card {
    position: absolute;
    left: 250px;
    width: 700px;
    height: 400px;
    background: linear-gradient(115deg, var(--card-mid) 0%, var(--card-dark) 55%, #020b11 100%);
    border-left: 5px solid var(--brand-blue);
    border-bottom: 5px solid var(--brand-blue);
    box-shadow: 0 14px 30px rgba(0,0,0,.45);
    overflow: hidden;
  }
  .card--back { top: 35px; }
  .card--front { top: 465px; }

  /* Back */
  .back-brand {
    position: absolute;
    top: 110px; left: 0; right: 0;
    text-align: center;
  }
  .back-brand .wordmark {
    font-family: "Michroma", sans-serif;
    font-size: 44px;
    letter-spacing: 2px;
    color: var(--emboss);
    text-shadow: 0 1px 0 var(--emboss-light), 0 -1px 0 #000;
  }
  .back-brand .tagline {
    font-family: "Michroma", sans-serif;
    font-size: 11px;
    letter-spacing: 5px;
    color: var(--emboss);
    text-shadow: 0 1px 0 var(--emboss-light);
    margin-top: 2px;
  }
  .partner-badge {
    position: absolute;
    left: 50%; top: 255px;
    transform: translateX(-50%);
    width: 250px; height: 80px;
  }

  /* Front */
  .front-brand {
    position: absolute;
    top: 36px; left: 30px;
    display: flex; align-items: center; gap: 14px;
  }
  .front-brand .dot {
    width: 48px; height: 48px;
    border: 4px solid var(--brand-blue);
    border-radius: 50%;
  }
  .front-brand .wordmark {
    font-family: "Michroma", sans-serif;
    font-size: 30px;
    color: var(--brand-blue);
    letter-spacing: 1px;
    line-height: 1;
  }
  .front-brand .tagline {
    font-family: "Michroma", sans-serif;
    font-size: 9px;
    letter-spacing: 4px;
    color: var(--white);
    margin-top: 4px;
  }
  .person {
    position: absolute;
    top: 112px; right: 34px;
    text-align: right;
  }
  .person .name {
    font-family: "Michroma", sans-serif;
    font-size: 20px;
    color: var(--brand-blue);
    letter-spacing: 1px;
  }
  .person .role {
    font-size: 19px;
    color: var(--white);
    margin-top: 4px;
  }
  .accent-bar {
    position: absolute;
    top: 160px; right: 0;
    width: 8px; height: 42px;
    background: var(--brand-blue);
  }
  .contact {
    position: absolute;
    left: 42px; top: 200px;
    color: var(--white);
    font-size: 20px;
    line-height: 1.25;
  }
  .contact .address { margin-bottom: 14px; }
  .contact ul { list-style: none; }
  .contact li {
    display: flex; align-items: center; gap: 12px;
    margin-bottom: 8px;
  }
  .contact svg { width: 20px; height: 20px; flex: none; }
  .emblem {
    position: absolute;
    right: 30px; top: 165px;
    width: 210px; height: 210px;
    border: 12px solid var(--ring-blue);
    border-radius: 50%;
    display: flex; align-items: center; justify-content: center;
  }
  .emblem span {
    font-family: "Michroma", sans-serif;
    font-size: 22px;
    color: var(--white);
    letter-spacing: 1px;
  }
</style>
</head>
<body>

  <section class="card card--back">
    <div class="back-brand">
      <div class="wordmark">KESTROVA</div>
      <div class="tagline">ELECTRICAL SOLUTIONS</div>
    </div>
    <svg class="partner-badge" viewBox="0 0 250 80" role="img" aria-label="Tarrow Alliance partner badge">
      <rect x="1" y="1" width="248" height="78" rx="8" fill="none" stroke="var(--bronze)" stroke-width="1.5"/>
      <rect x="16" y="14" width="52" height="52" rx="5" fill="var(--white)"/>
    </svg>
  </section>

  <section class="card card--front">
    <div class="front-brand">
      <div class="dot"></div>
      <div>
        <div class="wordmark">KESTROVA</div>
        <div class="tagline">ELECTRICAL SOLUTIONS</div>
      </div>
    </div>

    <div class="person">
      <div class="name">MARLOW DENNING</div>
      <div class="role">Manager</div>
    </div>
    <div class="accent-bar"></div>

    <div class="contact">
      <p class="address">Your Address, City<br>State, Zip 0000</p>
      <ul>
        <li>
          <svg viewBox="0 0 24 24" fill="none" stroke="var(--brand-blue)" stroke-width="2"><path d="M5 3h4l2 5-2.5 1.5a11 11 0 0 0 6 6L16 13l5 2v4a2 2 0 0 1-2 2A17 17 0 0 1 3 5a2 2 0 0 1 2-2z"/></svg>
          123-456-2100
        </li>
        <li>
          <svg viewBox="0 0 24 24" fill="none" stroke="var(--brand-blue)" stroke-width="2"><rect x="3" y="5" width="18" height="14" rx="1"/><path d="M3 6l9 7 9-7"/></svg>
          youremail@mailbox.com
        </li>
        <li>
          <svg viewBox="0 0 24 24" fill="none" stroke="var(--brand-blue)" stroke-width="2"><circle cx="12" cy="12" r="9"/><path d="M3 12h18M12 3c3 3 3 15 0 18M12 3c-3 3-3 15 0 18"/></svg>
          www.yourwebsite.com
        </li>
      </ul>
    </div>

    <div class="emblem"><span>KESTROVA</span></div>
  </section>

</body>
</html>
```